Patent Law

Need to develop a home page for a patent lawyer.

Colors should go with logo, blues...

Company Name- Corvel Tindry, PLLC

Company Overview-

I am an Intellectual Property Lawyer and focus on patents, copyrights, trademarks, & trade secrets. I work with small businesses and start ups in the chemical and biotech industries.

Why Us-

I am small firm that can provide large-firm service at a reasonable price. I also can charge flat-fees for entreprenuers in certain practice areas.

Services-
Intellectual Property
Patents
Copyrights
Trademarks
Trade secrets
Healthcare Compliance
Elder law
Wills
Trusts

Website we like-
http://www.quarnlowtide.example/ - within industry!!
http://www.vopperhask.example/
http://dulbrickovan.example/
http://thefernwoldguides.example/

Target Market(s)

My customers will be small business, specifically small start-up companies in the chemical and biotech arena.

Industry/Entity Type

Trade

Requirements
Must have
• Colors should go with logo, blues...

```html
<!DOCTYPE html>
<html lang="en">
<head>
<meta charset="utf-8">
<title>Corvel Tindry, PLLC — Patent Law</title>
<link href="https://fonts.googleapis.com/css2?family=Alegreya+Sans:ital,wght@0,400;0,500;0,700;0,800;1,400&display=swap" rel="stylesheet">
<style>
  :root{
    --blue:#0a8fe0;
    --blue-bright:#1196e6;
    --navy:#1e2468;
    --navy-text:#1f2a78;
    --ink:#3b3e44;
    --grey-edge:#b9bcc0;
    --white:#ffffff;
    --footer-top:#0a7fd4;
    --footer-bottom:#1e2468;
  }
  *{box-sizing:border-box;margin:0;padding:0}
  html,body{width:1200px;height:1000px;overflow:hidden}
  body{position:relative;background:var(--white);font-family:"Alegreya Sans",sans-serif;color:var(--ink)}

  .top-strip{position:absolute;left:0;top:0;width:1200px;height:7px;background:var(--blue)}
  .site-header{position:absolute;left:0;top:7px;width:1200px;height:108px;background:var(--white);box-shadow:0 3px 4px rgba(0,0,0,.25)}
  .brand{position:absolute;left:157px;top:42px;display:flex;align-items:center;gap:10px}
  .brand-mark{width:26px;height:26px;border-radius:50%;background:var(--blue)}
  .brand-name{font-size:22px;font-weight:500;color:var(--ink);letter-spacing:.5px}
  .call-us{position:absolute;left:828px;top:36px;font-size:24px;font-weight:700;color:#4a4d52}
  .call-us span{color:var(--blue)}
  .main-nav{position:absolute;left:525px;top:83px;width:525px;height:32px}
  .main-nav svg{position:absolute;left:0;top:0}
  .main-nav ul{position:absolute;right:30px;top:0;height:32px;display:flex;gap:22px;list-style:none;align-items:center}
  .main-nav li{font-size:13px;color:var(--white);font-weight:500}
  .main-nav li.active{color:var(--navy)}

  .slider{position:absolute;left:176px;top:134px;width:849px;height:358px;border-radius:10px;background:linear-gradient(#f4f4f4,#d9d9d9);border:1px solid #c8c8c8;box-shadow:0 12px 10px -8px rgba(0,0,0,.35)}
  .slide-photo{position:absolute;left:13px;top:13px;width:823px;height:327px;border-radius:6px;background:linear-gradient(100deg,#8aa1c4 0%,#cfd6e0 30%,#d9dde3 55%,#b8c0cc 80%,#9aa7b9 100%)}
  .slide-arrow{position:absolute;top:278px;width:42px;height:42px;border-radius:50%;background:radial-gradient(circle at 50% 35%,#fff,#cfcfcf);border:1px solid #b5b5b5;box-shadow:0 0 0 8px #ededed,0 0 0 9px #cfcfcf}
  .slide-arrow svg{position:absolute;left:9px;top:11px}
  .slide-arrow.prev{left:156px}
  .slide-arrow.next{left:1005px}

  .card{position:absolute;top:512px;width:264px;height:326px;border-radius:26px 26px 26px 26px;background:linear-gradient(#0a90e2 0%,#0a7fd4 35%,#1e2468 100%);border:5px solid var(--grey-edge);box-shadow:inset 0 0 0 1px #e2e4e7}
  .card.why{left:154px}
  .card.what{left:467px}
  .card.contact{left:780px}
  .card-tab{position:absolute;left:0;top:12px;width:234px;height:40px;border-radius:0 6px 6px 0;background:linear-gradient(90deg,#8d9196 0%,#e6e7e9 55%,#ffffff 100%);box-shadow:0 3px 3px rgba(0,0,0,.3);display:flex;align-items:center;justify-content:center;font-size:23px;font-weight:800;color:var(--navy-text);letter-spacing:.3px}
  .card-icon{position:absolute;left:87px;top:68px;width:71px;height:59px;border:2px solid var(--white)}
  .card-icon svg{display:block}
  .card-text{position:absolute;left:13px;top:150px;width:245px;font-size:12.3px;line-height:20.6px;font-style:italic;color:var(--white)}
  .services{position:absolute;left:0;top:0;list-style:none}
  .services li{position:absolute;font-size:13px;line-height:12px;font-style:italic;color:var(--white);width:90px}
  .services li::before{content:"";position:absolute;left:-17px;top:1px;border-left:8px solid var(--white);border-top:5px solid transparent;border-bottom:5px solid transparent}

  .site-footer{position:absolute;left:0;top:860px;width:1200px;height:140px;background:linear-gradient(var(--footer-top),var(--footer-bottom))}
  .footer-map{position:absolute;left:161px;top:21px;width:219px;height:101px;border-radius:40px;background:radial-gradient(ellipse,#d6d8dc 0%,#b9bcc2 60%,rgba(185,188,194,0) 75%)}
  .footer-nav{position:absolute;left:452px;top:92px;display:flex;gap:18px;list-style:none}
  .footer-nav li{font-size:10px;color:var(--white)}
  .copyright{position:absolute;left:452px;top:108px;width:326px;text-align:center;font-size:9.5px;color:var(--white)}
  .footer-brand{position:absolute;left:862px;top:60px;display:flex;align-items:center;gap:8px}
  .footer-brand .brand-mark{width:22px;height:22px;background:var(--white)}
  .footer-brand .brand-name{font-size:19px;color:var(--white)}
</style>
</head>
<body>
  <div class="top-strip"></div>
  <header class="site-header">
    <div class="brand"><span class="brand-mark"></span><span class="brand-name">Corvel Tindry, PLLC</span></div>
    <div class="call-us">CALL US : <span>444-555-019</span></div>
  </header>
  <nav class="main-nav">
    <svg width="525" height="32" viewBox="0 0 525 32"><polygon points="46,0 525,0 525,32 0,32" fill="#0a8fe0"/></svg>
    <ul>
      <li class="active">HOME</li><li>ABOUT</li><li>PRACTICES</li><li>PEOPLE</li><li>BLOGS</li><li>NEWS</li><li>CONTACT</li>
    </ul>
  </nav>

  <section class="slider">
    <div class="slide-photo" role="img" aria-label="Photo of a smiling couple meeting with a lawyer at a desk"></div>
  </section>
  <div class="slide-arrow prev"><svg width="22" height="18" viewBox="0 0 22 18"><path d="M9 1 L1 9 L9 17 L9 12 L21 12 L21 6 L9 6 Z" fill="#9a9a9a"/></svg></div>
  <div class="slide-arrow next"><svg width="22" height="18" viewBox="0 0 22 18"><path d="M13 1 L21 9 L13 17 L13 12 L1 12 L1 6 L13 6 Z" fill="#9a9a9a"/></svg></div>

  <section class="card why">
    <div class="card-tab">WHY US</div>
    <div class="card-icon">
      <svg width="67" height="55" viewBox="0 0 67 55"><path d="M14 16 L14 48 L21 41 L26 52 L31 50 L26 39 L35 39 Z" fill="#fff"/><path d="M39 16 q0-9 9-9 q9 0 9 8 q0 5-6 8 q-3 2-3 6 v2" fill="none" stroke="#fff" stroke-width="4"/><circle cx="48" cy="38" r="2.6" fill="#fff"/></svg>
    </div>
    <p class="card-text">I am an Intellectual Property Lawyer and focus on patents, copyrights, trademarks, &amp; trade secrets. I work with small businesses and start ups in the chemical and biotech industries.<br>I am small firm that can provide large-firm service at a reasonable price. I also can charge flat-fees for entreprenuers in certain practice areas.</p>
  </section>

  <section class="card what">
    <div class="card-tab">WHAT WE DO</div>
    <div class="card-icon">
      <svg width="67" height="55" viewBox="0 0 67 55"><g fill="none" stroke="#fff" stroke-width="2.5"><circle cx="17" cy="12" r="5"/><circle cx="17" cy="27" r="5"/><circle cx="17" cy="42" r="5"/><path d="M14 12 l3 3 l6-7 M14 27 l3 3 l6-7"/><path d="M29 10 h25 M29 15 h18 M29 25 h25 M29 30 h18 M29 40 h25 M29 45 h18"/></g></svg>
    </div>
    <ul class="services">
      <li style="left:43px;top:153px">Intellectual Property</li>
      <li style="left:43px;top:188px">Copyrights</li>
      <li style="left:43px;top:211px">Trade secrets</li>
      <li style="left:43px;top:233px">Elder law</li>
      <li style="left:43px;top:256px">Trusts</li>
      <li style="left:168px;top:153px">Patents</li>
      <li style="left:168px;top:175px">Trademarks</li>
      <li style="left:168px;top:198px">Healthcare Compliance</li>
      <li style="left:168px;top:243px">Wills</li>
    </ul>
  </section>

  <section class="card contact">
    <div class="card-tab">CONTACT</div>
    <div class="card-icon">
      <svg width="67" height="55" viewBox="0 0 67 55"><g fill="none" stroke="#fff" stroke-width="3" stroke-linejoin="round" stroke-linecap="round"><path d="M6 20 L18 12 L30 16 L40 12 L61 22"/><path d="M10 30 L24 44 Q28 47 31 44 L50 28"/><path d="M30 16 L22 24 Q25 28 31 24 L36 21"/><path d="M27 36 L34 42 M32 32 L40 38 M37 28 L44 34"/></g></svg>
    </div>
    <p class="card-text">I am an Intellectual Property Lawyer and focus on patents, copyrights, trademarks, &amp; trade secrets. I work with small businesses and start ups in the chemical and biotech industries.<br>I am small firm that can provide large-firm service at a reasonable price. I also can charge flat-fees for entreprenuers in certain practice areas.</p>
  </section>

  <footer class="site-footer">
    <div class="footer-map" role="img" aria-label="Grey world map"></div>
    <ul class="footer-nav">
      <li>HOME</li><li>ABOUT</li><li>PRACTICES</li><li>PEOPLE</li><li>BLOGS</li><li>NEWS</li><li>CONTACT</li>
    </ul>
    <p class="copyright">copyright@Corvel Tindry, PLLC all reserved.</p>
    <div class="footer-brand"><span class="brand-mark"></span><span class="brand-name">Corvel Tindry, PLLC</span></div>
  </footer>
</body>
</html>
```